Vietnamese Restaurant Poster

We are a family restaurant specializing in Vietnamese comfort food of pho (Vietnamese Beef Noodle Soup).

We need to create a poster that will attract customers driving by our restaurant.

This poster will be placed on sandwich boards and placed on the intersecting streets.

We want it to be
- big and visually appealing.
- Preferably with a logo incorporating our name and a bowl of Pho
- a arrow sign pointing right
- our phone number 604-381-7295

The name of our restaurant is:

Pho Lanh Dao (Title text)
Vietnamese Restaurant (smaller text)

Reason: We have narrowed it down to 2  designs that we absolutely love. Thank you to all who have submitted.

Target Market(s)

Caucasian people who have not tried Vietnamese food. Our location is a little hidden so we want to make these posters to put on the main streets which will grab attention of people driving by to come into our restaurant

Industry/Entity Type

Restaurant

Requirements
Must have
• - big and visually appealing.
logo incorporating our name and a bowl of Pho
Nice to have
• a person eating a bowl of pho

```html
<!DOCTYPE html>
<html lang="en">
<head>
<meta charset="utf-8">
<title>Pho Lanh Dao — Vietnamese Restaurant</title>
<link rel="stylesheet" href="https://fonts.googleapis.com/css2?family=Montserrat:wght@800&family=Lato:wght@400;700;900&display=swap">
<style>
  :root {
    --plum: #3b2548;
    --white: #ffffff;
    --mauve: #a596a6;
    --broth-light: #f2ede4;
    --broth-mid: #d9cbb4;
    --herb: #8fa46a;
  }
  html, body {
    margin: 0;
    padding: 0;
    overflow: hidden;
    background: var(--plum);
  }
  .poster {
    position: relative;
    width: 801px;
    height: 1200px;
    background: var(--plum);
    overflow: hidden;
  }
  .brand-name {
    position: absolute;
    left: 50px;
    top: 22px;
    margin: 0;
    font-family: "Montserrat", sans-serif;
    font-weight: 800;
    font-size: 182px;
    line-height: 136px;
    letter-spacing: -4px;
    color: var(--white);
    text-transform: uppercase;
  }
  .brand-name span { display: block; padding-top: 18px; }
  .tagline {
    position: absolute;
    left: 52px;
    top: 478px;
    margin: 0;
    font-family: "Lato", sans-serif;
    font-weight: 400;
    font-size: 70px;
    line-height: 66px;
    letter-spacing: -1px;
    color: var(--mauve);
    text-transform: uppercase;
  }
  .direction-arrow {
    position: absolute;
    left: 568px;
    top: 484px;
    width: 180px;
    height: 128px;
  }
  .dish-photo {
    position: absolute;
    left: 0;
    top: 660px;
    width: 801px;
    height: 370px;
    background:
      radial-gradient(ellipse 45% 55% at 40% 55%, var(--broth-mid) 0%, var(--broth-light) 70%),
      var(--broth-light);
  }
  .dish-photo::after {
    content: "";
    position: absolute;
    left: 300px;
    top: 40px;
    width: 260px;
    height: 120px;
    border-radius: 50%;
    background: radial-gradient(ellipse at center, var(--herb) 0%, transparent 70%);
    opacity: 0.5;
  }
  .phone {
    position: absolute;
    left: 52px;
    top: 1050px;
    margin: 0;
    font-family: "Lato", sans-serif;
    font-weight: 400;
    font-size: 104px;
    line-height: 120px;
    letter-spacing: -1px;
    color: var(--white);
    white-space: nowrap;
  }
  .phone-label {
    font-weight: 900;
    color: var(--mauve);
    margin-right: 18px;
  }
</style>
</head>
<body>
  <main class="poster">
    <h1 class="brand-name"><span>Pho</span><span>Lanh</span><span>Dao</span></h1>
    <p class="tagline">Vietnamese<br>Restaurant</p>
    <svg class="direction-arrow" viewBox="0 0 180 128" aria-hidden="true">
      <path d="M6 64 H150 M104 18 L150 64 L104 110" fill="none" stroke="var(--mauve)" stroke-width="34" stroke-linecap="round" stroke-linejoin="round"/>
    </svg>
    <div class="dish-photo" role="img" aria-label="Photo of a white bowl of beef pho with rice noodles, sliced beef, meatballs, chili, bean sprouts and Thai basil, with a lemon wedge on the side"></div>
    <p class="phone"><span class="phone-label">T</span>604 381 7295</p>
  </main>
</body>
</html>
```